Business Card Design Project : Tidewell Press

In preparation for market launch, Whistler's Tidewell Press require the development of a business card. Tidewell Press is a Community online publishing web portal. We provide the the city of Whistler located in B.C. (Canada) business directories, News, Classified ads, News, Events and blogs etc.

The main focus of the brand is to help local businesses to corporate with their online advertisement and marketing. Meeting our clients face to face is a must (B2B).

Target Market(s)

The target market is B2B customers. Business Owners to Marketing, advertising Managers

Industry/Entity Type

Business

Requirements
Must have
• - The business card will be two sided.
the BACK side will have our logo which consist of (icon, url,slogan) submited. The logo will be middle and centred.

The FRONT side should have company details:

Company Legal Name: FERNDALE TIDEWELL PRESS

Owen Marsk
Director of Sales & Marketing

www.ferndaletidewell.biz
owen@ferndaletidewell.biz

Phone: 555 014 3826
#2817 - 562 E. Harlow Ave.
Vancouver, B.C. K7P2R4 Canada
Nice to have
• - For the "FRONT" side of our business card. You can separate or re-arrange with our logo components (icon, logo,slogan). It does not have to be together.

Also our company legal name is rather long so arrange or organize the name in a way to make it shorter. Your experience and creativity will have to come in play.
Should not have
• should not have other colors beside logo color and black text (2 colors). Also nothing Three dimensional

```html
<!DOCTYPE html>
<html lang="en">
<head>
<meta charset="utf-8">
<title>Tidewell Press – Business Card</title>
<link rel="stylesheet" href="https://fonts.googleapis.com/css2?family=Source+Sans+3:wght@400;600;700&display=swap">
<style>
  :root {
    --backdrop: #4b4b4b;
    --card: #ffffff;
    --ink: #1d1d1d;
    --brand-blue: #1b7ac4;
  }
  html, body {
    margin: 0;
    padding: 0;
    width: 1200px;
    height: 907px;
    overflow: hidden;
    background: var(--backdrop);
    font-family: "Source Sans 3", "Helvetica Neue", Arial, sans-serif;
  }
  .canvas {
    position: relative;
    width: 1200px;
    height: 907px;
  }
  .card {
    position: absolute;
    top: 148px;
    width: 380px;
    height: 622px;
    background: var(--card);
    border-radius: 19px;
  }
  .card--front { left: 203px; }
  .card--back  { left: 622px; }

  /* Front side */
  .company-name {
    position: absolute;
    top: 190px;
    right: 103px;
    margin: 0;
    text-align: right;
    color: var(--ink);
    font-weight: 700;
    font-size: 27px;
    line-height: 29px;
    letter-spacing: -0.3px;
  }
  .company-mark {
    position: absolute;
    top: 228px;
    left: 70px;
    width: 44px;
    height: 44px;
    border-radius: 50%;
    background: var(--brand-blue);
  }
  .person-name {
    position: absolute;
    top: 336px;
    left: 70px;
    margin: 0;
    color: var(--brand-blue);
    font-weight: 700;
    font-size: 25px;
    line-height: 28px;
    letter-spacing: -0.3px;
  }
  .person-title {
    position: absolute;
    top: 364px;
    left: 70px;
    margin: 0;
    color: var(--brand-blue);
    font-weight: 400;
    font-size: 18px;
    line-height: 22px;
  }
  .contact {
    position: absolute;
    top: 457px;
    left: 70px;
    margin: 0;
    color: var(--ink);
    font-style: normal;
    font-weight: 400;
    font-size: 17.5px;
    line-height: 21px;
  }

  /* Back side */
  .back-lockup {
    position: absolute;
    left: 0;
    right: 0;
    top: 410px;
    text-align: center;
  }
  .back-name {
    margin: 0;
    color: var(--brand-blue);
    font-weight: 700;
    font-size: 34px;
    line-height: 40px;
    letter-spacing: -0.3px;
  }
  .back-url {
    margin: 46px 0 0;
    color: var(--ink);
    font-weight: 700;
    font-size: 24px;
    line-height: 28px;
    letter-spacing: -0.4px;
  }
  .back-slogan {
    margin: 0;
    color: var(--brand-blue);
    font-weight: 400;
    font-size: 20px;
    line-height: 24px;
  }
</style>
</head>
<body>
  <main class="canvas">
    <section class="card card--front" aria-label="Card front">
      <span class="company-mark" aria-hidden="true"></span>
      <h1 class="company-name">FERNDALE<br>TIDEWELL<br>PRESS</h1>
      <p class="person-name">OWEN MARSK</p>
      <p class="person-title">Director of Sales &amp; Marketing</p>
      <address class="contact">
        #2817 - 562 E. Harlow Ave.<br>
        Vancouver, B.C. K7P2R4 Canada<br>
        Phone: 555 014 3826<br>
        owen@ferndaletidewell.biz
      </address>
    </section>

    <section class="card card--back" aria-label="Card back">
      <div class="back-lockup">
        <p class="back-name">Tidewell Press</p>
        <p class="back-url">www.ferndaletidewell.biz</p>
        <p class="back-slogan">Your information gateway</p>
      </div>
    </section>
  </main>
</body>
</html>
```